Web tool bar Project

I'm open to paying more if the quality of the bar is very good... if you feel the scope of the project does not match budget..... please quote me.

I need someone to re-design my web tool bar.

In the first attachment you can see a black tool bar (fig1). This is my old design. I want this to be the template as it shows what the text will say and where the buttons will be placed.

For the new tool bar:
-I would like the it to be white in colour (like fig.2)
-I would like the buttons to also be white. But the buttons must stand out so the designer should use the right shading to make the buttons stand out.
-The bar needs to be the quality of the bar in fig.2 (very good quality). I have had many designs done for this but no designer seems to be good enough to get the right quality.
-The text in the white boxes on the new bar should be the colours shown above the buttons next to fig.1 (blue, green, red, yellow, purple & orange).

Finally please put the logo attached (DV) at the end of the bar on the right where it says logo. The logo should blend in well with the bar as it has white in it also.

Please take note of fig.2 it is good quality with sharp edges I would like the same quality.

Any further questions please ask?

Requirements
Must have
• Quality!

```html
<!DOCTYPE html>
<html lang="en">
<head>
<meta charset="utf-8">
<title>Daily Venue Toolbar</title>
<link href="https://fonts.googleapis.com/css2?family=Signika:wght@600&display=swap" rel="stylesheet">
<style>
  :root {
    --bar-top: #f4f4f4;
    --bar-bottom: #cfcfcf;
    --bar-edge: #b9b9b9;
    --btn-top: #ffffff;
    --btn-bottom: #e6e6e6;
    --btn-border: #b3b3b3;
    --blue: #2a7da7;
    --green: #6bab2b;
    --red: #c4302b;
    --yellow: #e6b70a;
    --purple: #9a4ea6;
    --orange: #ef7a27;
    --brand: #1a8fd6;
    --page: #ffffff;
  }
  * { box-sizing: border-box; margin: 0; padding: 0; }
  html, body { width: 1200px; height: 200px; overflow: hidden; background: var(--page); }
  .toolbar {
    position: relative;
    width: 1200px;
    height: 60px;
    background: linear-gradient(to bottom, var(--bar-top), var(--bar-bottom));
    border-bottom: 1px solid var(--bar-edge);
    box-shadow: 0 2px 4px rgba(0,0,0,0.25);
    font-family: "Signika", "Trebuchet MS", sans-serif;
  }
  .tool-button {
    position: absolute;
    top: 12px;
    height: 36px;
    display: flex;
    align-items: center;
    justify-content: center;
    gap: 8px;
    border: 1px solid var(--btn-border);
    border-radius: 4px;
    background: linear-gradient(to bottom, var(--btn-top), var(--btn-bottom));
    box-shadow: inset 0 1px 0 #fff, 0 1px 1px rgba(0,0,0,0.08);
    font-size: 14px;
    font-weight: 600;
    white-space: nowrap;
  }
  .tool-button svg { width: 14px; height: 14px; flex: none; }
  .login    { left: 11px;  width: 190px; color: var(--blue); }
  .check-in { left: 380px; width: 110px; color: var(--green); }
  .friends  { left: 495px; width: 240px; color: var(--red); }
  .feeds    { left: 740px; width: 140px; color: var(--yellow); }
  .messages { left: 885px; width: 120px; color: var(--purple); }
  .scrapbook{ left: 1010px; width: 120px; color: var(--orange); }
  .brand-name {
    position: absolute;
    left: 1148px;
    top: 16px;
    width: 42px;
    text-align: center;
    font-size: 21px;
    font-weight: 600;
    line-height: 28px;
    color: var(--brand);
  }
</style>
</head>
<body>
  <nav class="toolbar">
    <div class="tool-button login">
      <svg viewBox="0 0 14 14"><circle cx="7" cy="4" r="3.2" fill="currentColor"/><path d="M1.5 14c0-3.6 2.4-5.6 5.5-5.6s5.5 2 5.5 5.6z" fill="currentColor"/></svg>
      Daily Venue Login
    </div>
    <div class="tool-button check-in">
      <svg viewBox="0 0 14 14"><path d="M7 0.5a4.3 4.3 0 0 0-4.3 4.3C2.7 8 7 13.5 7 13.5s4.3-5.5 4.3-8.7A4.3 4.3 0 0 0 7 0.5zm0 6.1a1.7 1.7 0 1 1 0-3.4 1.7 1.7 0 0 1 0 3.4z" fill="currentColor"/></svg>
      Check In
    </div>
    <div class="tool-button friends">
      <svg viewBox="0 0 18 14" style="width:18px"><circle cx="6" cy="4" r="3" fill="currentColor"/><path d="M0.5 13.5c0-3.4 2.3-5.2 5.5-5.2s5.5 1.8 5.5 5.2z" fill="currentColor"/><circle cx="12.5" cy="4.5" r="2.5" fill="currentColor"/><path d="M12.5 8.5c2.8 0 5 1.6 5 5h-5z" fill="currentColor"/></svg>
      Online Friends at Circlenet
    </div>
    <div class="tool-button feeds">
      <svg viewBox="0 0 14 14"><circle cx="2.2" cy="11.8" r="1.8" fill="currentColor"/><path d="M0.5 5.2a8.3 8.3 0 0 1 8.3 8.3" stroke="currentColor" stroke-width="2.2" fill="none"/><path d="M0.5 0.8a12.7 12.7 0 0 1 12.7 12.7" stroke="currentColor" stroke-width="2.2" fill="none"/></svg>
      Venue Feeds
    </div>
    <div class="tool-button messages">
      <svg viewBox="0 0 14 14"><ellipse cx="7" cy="6" rx="6.5" ry="4.8" fill="currentColor"/><path d="M2.5 9l-1 4 4-2.6z" fill="currentColor"/></svg>
      Messages
    </div>
    <div class="tool-button scrapbook">
      <svg viewBox="0 0 14 14"><rect x="1.5" y="3" width="11" height="8" rx="1" transform="rotate(-25 7 7)" fill="none" stroke="currentColor" stroke-width="1.4"/><path d="M5 4.8l2.4 5" stroke="currentColor" stroke-width="1.2"/></svg>
      Scrapbook
    </div>
    <div class="brand-name">DV</div>
  </nav>
</body>
</html>
```